Stationary and Logo Design Project

We need a full corporate logo and stationary design for our company Lumvira7Q. Lumvira7Q specializes in creating custom adult sex toys using CAD and 3D Printing technologies as part of the process. The companies tagline is "your desire, your design", though this is not required to be part of the logo.

We are looking for something sensual, romantic and sexy, but not something explicit and vulgar.

As the company will be targeting mid to high-end clientele tastefulness is very important to us - this is difficult when the service we are selling is sex but can be achieved.

What we are after:

1. Logo
2. Business Card Design
3. Letterhead Design
4. Email Signature Design

File Formats we require in colour, greyscale and Black and White:

1 .AI
2 .EPS
3 .TIF
4 .PDF
5 .PNG (300 dpi)
6 .JPG (300 dpi)
7 .GIF (300 dpi)

Target Market(s)

Adults between the ages of 21 and 50 (Predominantly female but not limited to) who like there sex toys and want a custom job.

Industry/Entity Type

Adult

Requirements
Must have
• As we are planning on advertising in the future make sure the art is suitable for print advertising.
Nice to have
• The tagline "your desire, your design" on the business card, letterhead and email signature.
Should not have
• Explicit/vulgar illustrations.

"Clip-Art" should not be used.

```html
<!DOCTYPE html>
<html lang="en">
<head>
<meta charset="utf-8">
<title>Lumvira7Q – Business Cards</title>
<link href="https://fonts.googleapis.com/css2?family=Arimo:wght@400;700&display=swap" rel="stylesheet">
<style>
  :root {
    --backdrop: #2b2b2b;
    --card-white: #f7f7f7;
    --card-grey: #e4e4e4;
    --ink: #111111;
    --ink-soft: #333333;
    --accent: #d71920;
    --wine-dark: #1e0606;
    --wine-mid: #3d0c0c;
    --wine-light: #6a1616;
    --paper-light: #ffffff;
  }
  * { margin: 0; padding: 0; box-sizing: border-box; }
  html, body {
    width: 1200px;
    height: 900px;
    overflow: hidden;
    background: var(--backdrop);
    font-family: "Arimo", Arial, sans-serif;
  }
  .canvas {
    position: relative;
    width: 1200px;
    height: 900px;
  }
  .card {
    position: absolute;
    left: 340px;
    width: 520px;
    height: 297px;
    overflow: hidden;
    box-shadow: 0 14px 30px rgba(0,0,0,0.55);
  }
  /* Front: white contact card */
  .card--front {
    top: 118px;
    background: linear-gradient(135deg, var(--card-grey) 0%, var(--card-white) 45%, var(--paper-light) 100%);
  }
  .card--front .brand {
    position: absolute;
    left: 36px;
    top: 168px;
  }
  .brand-name {
    display: flex;
    align-items: center;
    gap: 8px;
    font-weight: 700;
    letter-spacing: -0.5px;
    line-height: 1;
  }
  .brand-dot {
    display: inline-block;
    border-radius: 50%;
    background: var(--accent);
  }
  .card--front .brand-name { font-size: 30px; color: var(--ink); }
  .card--front .brand-dot { width: 14px; height: 14px; }
  .card--front .tagline {
    margin-top: 4px;
    font-size: 13px;
    color: var(--ink);
    letter-spacing: 0.3px;
  }
  .contact {
    position: absolute;
    right: 34px;
    top: 40px;
    text-align: right;
    color: var(--ink-soft);
  }
  .contact-name {
    font-size: 17px;
    font-weight: 700;
    color: var(--accent);
  }
  .contact-role {
    font-size: 11px;
    margin-top: 2px;
    margin-bottom: 16px;
  }
  .contact-line {
    font-size: 11.5px;
    line-height: 1.45;
  }
  .contact-line .key { color: var(--accent); }
  .contact-address {
    font-size: 11.5px;
    margin-top: 18px;
  }
  /* Back: wine card */
  .card--back {
    top: 470px;
    background: radial-gradient(ellipse at 60% 35%, var(--wine-light) 0%, var(--wine-mid) 45%, var(--wine-dark) 100%);
  }
  .card--back .brand {
    position: absolute;
    left: 40px;
    top: 104px;
  }
  .card--back .brand-name { font-size: 46px; color: var(--paper-light); }
  .card--back .brand-dot { width: 20px; height: 20px; }
  .card--back .tagline {
    margin-top: 6px;
    font-size: 17px;
    color: var(--paper-light);
    letter-spacing: 0.4px;
  }
  .card--back .web {
    position: absolute;
    left: 40px;
    top: 222px;
    font-size: 14px;
    letter-spacing: 2px;
    color: var(--accent);
  }
</style>
</head>
<body>
<main class="canvas">
  <section class="card card--front" aria-label="Business card front">
    <div class="brand">
      <div class="brand-name">Lumvira7Q <span class="brand-dot"></span></div>
      <div class="tagline">your desire, your design</div>
    </div>
    <div class="contact">
      <div class="contact-name">Marina Keller</div>
      <div class="contact-role">Manager</div>
      <div class="contact-line">(555) 210-4471 <span class="key">: p</span></div>
      <div class="contact-line">mkeller@lumvira7q.com <span class="key">: e</span></div>
      <div class="contact-line">www.lumvira7q.com <span class="key">: w</span></div>
      <div class="contact-address">1840 Orchard Ln., Fairhaven, OR 9710</div>
    </div>
  </section>

  <section class="card card--back" aria-label="Business card back">
    <div class="brand">
      <div class="brand-name">Lumvira7Q <span class="brand-dot"></span></div>
      <div class="tagline">your desire, your design</div>
    </div>
    <div class="web">www.Lumvira7Q.com</div>
  </section>
</main>
</body>
</html>
```